New graphics package for website

We're currently about to launch a product to insurance agents and we need to upgrade the graphics package for tundlex.io
The current site is http://tundlex.io
We'd like to upgrade the graphics package for this site - very simple. The site needs to have a very modern and elegant feel.
The site content should remain, we may add some. You can use lorem ipsum you need content to fill a space.
We need to add 3 page links - Home, Enroll, Request invitation
We also have an invitation page that needs to be upgraded (shall not be accessible from main site), the current page for that is: http://www.tundlex.io/webinar.php - content on this page cannot change, just needs a graphics over lay.
Final source files shall be AI or PSD and include all fonts and high-res images included.
Target Market(s)
Business to business - insurance agencies across the US are the only users of this site.
Industry/Entity Type
Insurance
Number of Pages Required
2 page
Requirements
Must have
- Multiple forms only in the inner pages:
- Enroll form for the enroll page.
- Invite form for the invite page
- Invite form shall only have name, email, phone, carrier

```html
<!DOCTYPE html>
<html lang="en">
<head>
<meta charset="utf-8">
<title>Tundlex.io — Insurance Marketing</title>
<link href="https://fonts.googleapis.com/css2?family=Oswald:wght@400;500;600&family=Open+Sans:wght@400;600;700&family=Dancing+Script:wght@600&display=swap" rel="stylesheet">
<style>
:root{
  --navy:#1c2536;
  --navy-deep:#141b28;
  --orange:#f7941d;
  --orange-dark:#e07f0c;
  --ink:#333a44;
  --muted:#8a9099;
  --light:#f4f5f7;
  --line:#e2e4e8;
  --white:#ffffff;
}
*{box-sizing:border-box;margin:0;padding:0}
html,body{width:674px;height:1200px;overflow:hidden}
body{font-family:"Open Sans",Arial,sans-serif;color:var(--ink);background:var(--white);font-size:7px;line-height:1.5}
.brand{font-family:"Open Sans",Arial,sans-serif;font-weight:600;font-size:18px;color:var(--white);letter-spacing:.2px}

/* header + hero */
.hero{position:relative;height:360px}
.hero-photo{position:absolute;inset:0;background:linear-gradient(100deg,#cdd3d6 0%,#b7bfc2 35%,#8f9aa0 60%,#6e7b80 100%)}
.site-header{position:absolute;top:0;left:0;right:0;height:40px;background:rgba(20,27,40,.92);display:flex;align-items:center;justify-content:space-between;padding:0 26px}
.header-right{text-align:right;color:var(--white)}
.call{font-size:6px;letter-spacing:.5px;margin-bottom:3px}
.call b{font-weight:700;margin-left:6px}
.main-nav{display:flex;gap:14px;font-size:6.5px;font-weight:600;letter-spacing:.4px}
.main-nav span{padding-bottom:2px}
.main-nav .active{border-bottom:1px solid var(--orange)}
.hero-copy{position:absolute;left:395px;top:130px;width:262px;color:var(--white);text-align:center}
.hero-copy h1{font-family:"Oswald",sans-serif;font-weight:500;font-size:19px;letter-spacing:.6px;line-height:1.15;white-space:nowrap}
.hero-copy h2{font-family:"Oswald",sans-serif;font-weight:400;font-size:15px;letter-spacing:.8px;margin-bottom:8px;white-space:nowrap}
.hero-copy p{font-size:6.5px;margin:0 10px 14px}
.btn{display:inline-block;background:var(--orange);color:var(--white);font-family:"Oswald",sans-serif;font-size:7.5px;letter-spacing:.8px;padding:7px 16px}

/* intro */
.intro{height:205px;text-align:center;padding-top:16px}
.script{font-family:"Dancing Script",cursive;color:var(--orange);font-size:12px}
.section-title{font-family:"Oswald",sans-serif;font-weight:500;font-size:15px;color:var(--navy);letter-spacing:.8px}
.intro-text{width:430px;margin:8px auto 16px;color:var(--muted)}
.features{display:flex;justify-content:center;gap:38px}
.feature{width:140px}
.feature-icon{width:32px;height:32px;border-radius:50%;background:#dfe2e6;margin:0 auto 6px;display:flex;align-items:center;justify-content:center}
.feature-icon.square{border-radius:4px;background:var(--orange)}
.feature h3{font-family:"Oswald",sans-serif;font-weight:500;font-size:8px;letter-spacing:.5px;color:var(--navy);margin-bottom:3px}
.feature p{color:var(--muted);font-size:6px}

/* news */
.news{position:relative;height:265px;text-align:center;padding-top:16px}
.news-bg{position:absolute;inset:0;background:linear-gradient(180deg,#eceef1 0%,#d2d7dd 55%,#b9c1c9 100%)}
.news > *:not(.news-bg){position:relative}
.news .sub{width:420px;margin:6px auto 14px;color:var(--muted)}
.cards{display:flex;justify-content:center;gap:14px}
.card{width:296px;height:150px;background:var(--white);display:flex;text-align:left;box-shadow:0 1px 3px rgba(0,0,0,.12)}
.card-photo{position:relative;width:118px;height:100%;background:linear-gradient(160deg,#8fa3b4,#4e5f70)}
.date{position:absolute;top:8px;left:8px;width:22px;background:var(--white);text-align:center;font-size:5px;color:var(--ink)}
.date b{display:block;background:var(--orange);color:var(--white);font-size:9px;font-family:"Oswald",sans-serif}
.card-body{flex:1;padding:10px 10px 8px;display:flex;flex-direction:column}
.card-body h3{font-size:8.5px;font-weight:700;color:var(--navy);line-height:1.3;margin-bottom:5px}
.card-body p{color:var(--muted);font-size:6px}
.card-foot{margin-top:auto;display:flex;justify-content:space-between;align-items:center;border-top:1px solid var(--line);padding-top:5px;font-size:6px;color:var(--muted)}
.card-foot .btn{font-size:6px;padding:4px 8px;background:var(--navy)}

/* enroll */
.enroll{height:115px;background:var(--orange);text-align:center;color:var(--white);padding-top:18px}
.enroll h2{font-family:"Oswald",sans-serif;font-weight:500;font-size:17px;letter-spacing:1px;line-height:1.1}
.enroll h3{font-family:"Oswald",sans-serif;font-weight:400;font-size:10px;letter-spacing:.6px;margin-bottom:14px}
.enroll-form{display:flex;justify-content:center;gap:8px}
.field{width:118px;height:20px;background:var(--white);color:#a8adb4;font-size:6px;text-align:left;padding:5px 8px}
.enroll-btn{width:60px;height:20px;border:1px solid var(--white);font-family:"Oswald",sans-serif;font-size:7px;display:flex;align-items:center;justify-content:center;gap:4px}

/* testimonial */
.testimonial{height:115px;text-align:center;padding-top:14px;background:var(--light)}
.quote-marks{display:flex;justify-content:center;gap:4px;margin-bottom:8px}
.quote-marks span{width:18px;height:18px;border-radius:50%;background:var(--orange);color:var(--white);font-family:Georgia,serif;font-size:12px;line-height:22px}
.quote-marks span.alt{background:var(--navy)}
.testimonial blockquote{width:470px;margin:0 auto 8px;font-style:italic;color:var(--muted);font-size:6.5px}
.author{font-weight:700;color:var(--navy);font-size:6.5px}
.role{color:var(--muted);font-size:5.5px}

/* footer */
.site-footer{height:140px;background:var(--navy);color:#aeb5c1;position:relative}
.footer-cols{display:flex;padding:18px 26px 0;gap:30px}
.footer-about{width:200px}
.footer-about .brand{font-size:16px;margin-bottom:6px}
.footer-about p{font-size:5.5px;margin-bottom:8px}
.socials{display:flex;gap:6px}
.socials span{width:13px;height:13px;border-radius:50%;background:#3a455a}
.footer-col{width:110px}
.footer-title{font-family:"Oswald",sans-serif;font-weight:500;font-size:7.5px;color:var(--white);letter-spacing:.6px;margin-bottom:6px}
.footer-col li{list-style:none;font-size:6px;margin-bottom:3px}
.cert{width:130px}
.cert-badge{width:70px;height:24px;background:var(--white);border-radius:2px;margin-bottom:6px}
.cert p{font-size:5.5px}
.footer-bottom{position:absolute;left:0;right:0;bottom:0;height:20px;background:var(--navy-deep);display:flex;justify-content:space-between;align-items:center;padding:0 26px;font-size:5.5px;color:#7d8594}
</style>
</head>
<body>

<section class="hero">
  <div class="hero-photo" role="img" aria-label="Smiling insurance agent in a suit holding a folder in front of a suburban house"></div>
  <header class="site-header">
    <div class="brand">Tundlex.io</div>
    <div class="header-right">
      <div class="call">CALL ON THE ENQUIRY <b>(555) 014-2290</b></div>
      <nav class="main-nav"><span class="active">HOME</span><span>ENROLL</span><span>REQUEST INVITATION</span></nav>
    </div>
  </header>
  <div class="hero-copy">
    <h1>PROSPECTS ARE EVERY WHERE</h1>
    <h2>GET IN FRONT OF THEM</h2>
    <p>Lorem ipsum dolor sit amet consectetur adipiscing elit sed do eiusmod tempor incididunt ut labore et dolore magna aliqua.</p>
    <span class="btn">EXPLORE MORE &nbsp;›</span>
  </div>
</section>

<section class="intro">
  <div class="script">Making insurance leads obsolete</div>
  <h2 class="section-title">DOMINATE YOUR LOCAL INSURANCE MARKETS</h2>
  <p class="intro-text">A new type of insurance marketing product that takes the tools used by internet lead aggregators and offers them to insurance agents for a low monthly fee. Cut out the middle man by dispatching powerful ads to the web and leverage mobile device advertising to get your good quality prospects.</p>
  <div class="features">
    <div class="feature">
      <div class="feature-icon"><svg width="14" height="14" viewBox="0 0 14 14"><path d="M1 6h3v7H1zM5 13V6l3-5c1 0 2 1 1.5 2.5L9 5.5h3.5c.8 0 1.3.8 1 1.5l-2 5.5c-.2.3-.5.5-.9.5z" fill="#5b6472"/></svg></div>
      <h3>CERTIFIED AGENT</h3>
      <p>Lorem ipsum dolor sit amet consectetur adipiscing elit sed do eiusmod tempor incididunt labore.</p>
    </div>
    <div class="feature">
      <div class="feature-icon square"><svg width="14" height="14" viewBox="0 0 14 14"><path d="M2 4h10l-1 8H3zM5 4a2 2 0 0 1 4 0" fill="none" stroke="#fff" stroke-width="1.3"/></svg></div>
      <h3>SELLING PRODUCT</h3>
      <p>Lorem ipsum dolor sit amet consectetur adipiscing elit sed do eiusmod tempor incididunt labore.</p>
    </div>
    <div class="feature">
      <div class="feature-icon"><svg width="14" height="14" viewBox="0 0 14 14"><path d="M1 6.5L13 1 10 13 7 8.5z M7 8.5L13 1" fill="#5b6472" stroke="#5b6472" stroke-width=".6"/></svg></div>
      <h3>GET A FREE QUOTE</h3>
      <p>Lorem ipsum dolor sit amet consectetur adipiscing elit sed do eiusmod tempor incididunt labore.</p>
    </div>
  </div>
</section>

<section class="news">
  <div class="news-bg" role="img" aria-label="Faint city skyline in the background"></div>
  <h2 class="section-title">LATEST NEWS</h2>
  <p class="sub">Lorem ipsum dolor sit amet consectetur adipiscing elit sed do eiusmod tempor incididunt ut labore et dolore magna aliqua ut enim ad minim veniam.</p>
  <div class="cards">
    <article class="card">
      <div class="card-photo" role="img" aria-label="Businessman thinking at a desk"><div class="date"><b>21</b>JAN</div></div>
      <div class="card-body">
        <h3>Lorem ipsum dolor sit amet elit sed do eiusmod</h3>
        <p>Lorem ipsum dolor sit amet consectetur adipiscing elit sed do eiusmod tempor incididunt ut labore et dolore magna aliqua ut enim ad minim veniam quis nostrud.</p>
        <div class="card-foot"><span>Posted by Daniel Reeve</span><span class="btn">Read More</span></div>
      </div>
    </article>
    <article class="card">
      <div class="card-photo" role="img" aria-label="Business people under umbrellas"><div class="date"><b>21</b>JAN</div></div>
      <div class="card-body">
        <h3>Lorem ipsum dolor sit amet elit sed do eiusmod</h3>
        <p>Lorem ipsum dolor sit amet consectetur adipiscing elit sed do eiusmod tempor incididunt ut labore et dolore magna aliqua ut enim ad minim veniam quis nostrud.</p>
        <div class="card-foot"><span>Posted by Marcus Hale</span><span class="btn">Read More</span></div>
      </div>
    </article>
  </div>
</section>

<section class="enroll">
  <h2>ENROLL</h2>
  <h3>FOR TUNDLEX MARKETING</h3>
  <div class="enroll-form">
    <div class="field">Enter name</div>
    <div class="field">Enter email</div>
    <div class="field">Enter phone</div>
    <div class="enroll-btn">ENROLL <span>›</span></div>
  </div>
</section>

<section class="testimonial">
  <div class="quote-marks"><span>“</span><span class="alt">”</span></div>
  <blockquote>“ Lorem ipsum dolor sit amet consectetur adipiscing elit sed do eiusmod tempor incididunt ut labore et dolore magna aliqua. Ut enim ad minim veniam quis nostrud exercitation ullamco laboris nisi ut aliquip ex ea commodo consequat duis aute irure dolor. ”</blockquote>
  <div class="author">Daniel Reeve</div>
  <div class="role">Marketing Executive</div>
</section>

<footer class="site-footer">
  <div class="footer-cols">
    <div class="footer-about">
      <div class="brand">Tundlex.io</div>
      <p>Lorem ipsum dolor sit amet consectetur adipiscing elit sed do eiusmod tempor incididunt ut labore et dolore magna aliqua.</p>
      <div class="socials"><span></span><span></span><span></span><span></span></div>
    </div>
    <div class="footer-col">
      <h4 class="footer-title">SITEMAP</h4>
      <ul><li>Home</li><li>Enroll</li><li>Request invitation</li><li>Contact us</li></ul>
    </div>
    <div class="footer-col">
      <h4 class="footer-title">INSURANCE</h4>
      <ul><li>Lorem ipsum dolor</li><li>Consectetur adipiscing</li><li>Lorem ipsum dolor</li><li>Consectetur adipiscing</li></ul>
    </div>
    <div class="cert">
      <h4 class="footer-title">CERTIFIED BY NORVA</h4>
      <div class="cert-badge"></div>
      <p>We have been certified by Norva to provide the services to you. We are trusted and experienced in search marketing.</p>
    </div>
  </div>
  <div class="footer-bottom"><span>© Tundlex.io Professional Corporation</span><span>All rights reserved</span></div>
</footer>

</body>
</html>
```